Professional & attention grabbing.

A business card design, front and back. I already have a logo I will attach, but I am open to something new as well.
Things to include:
Name:
Title:
Phone:
Email:
Wanting something that is professional but attention grabbing.
Also we do a lot of work using drones on natural gas pipelines (leading the future)if you want to include any of that. I'm open to ideas.
Target Market(s)
Natural gas transmission industry / greenhouse gas mitigation industry
Industry/Entity Type
Business
Contact Information for Business Card
All details have been conveyed above.
Colors
Designer to choose colors to be used in the design.
Look and feel
Each slider illustrates characteristics of the customer's brand and the style your logo design should communicate.

```html
<!DOCTYPE html>
<html lang="en">
<head>
<meta charset="utf-8">
<title>KV Field Inspections – Business Card</title>
<link href="https://fonts.googleapis.com/css2?family=Poppins:wght@400;600&family=Work+Sans:wght@400;500&display=swap" rel="stylesheet">
<style>
  :root {
    --backdrop: #c9c9c9;
    --card-white: #ffffff;
    --card-dark: #2b2b2b;
    --accent-red: #b3161b;
    --ink: #3a3a3a;
    --silver: #bdbdbd;
    --mark-grey: #4a4a4a;
  }
  * { margin: 0; padding: 0; box-sizing: border-box; }
  html, body {
    width: 1200px;
    height: 1000px;
    overflow: hidden;
    background: var(--backdrop);
  }
  .card-set {
    position: relative;
    width: 1200px;
    height: 1000px;
  }
  .card {
    position: absolute;
    top: 355px;
    width: 510px;
    height: 291px;
    box-shadow: 0 3px 10px rgba(0,0,0,0.25);
  }
  .card--front { left: 60px; background: var(--card-white); }
  .card--back { left: 630px; background: var(--card-dark); }

  .identity {
    position: absolute;
    top: 124px;
    right: 270px;
    text-align: right;
    white-space: nowrap;
  }
  .identity__name {
    font-family: "Poppins", sans-serif;
    font-weight: 600;
    font-size: 18px;
    line-height: 1.1;
    color: var(--accent-red);
    letter-spacing: 0.3px;
  }
  .identity__title {
    font-family: "Work Sans", sans-serif;
    font-weight: 500;
    font-size: 13px;
    color: var(--ink);
    margin-top: 2px;
  }
  .divider {
    position: absolute;
    left: 254px;
    top: 124px;
    width: 2px;
    height: 42px;
    background: var(--accent-red);
  }
  .contact-list {
    position: absolute;
    left: 267px;
    top: 127px;
    list-style: none;
    font-family: "Work Sans", sans-serif;
    font-size: 13px;
    color: var(--ink);
    white-space: nowrap;
  }
  .contact-list li {
    display: flex;
    align-items: center;
    gap: 8px;
    height: 18px;
  }
  .contact-list svg { width: 10px; height: 10px; fill: var(--accent-red); }

  .brand {
    position: absolute;
    inset: 0;
    display: flex;
    align-items: center;
    justify-content: center;
    gap: 16px;
  }
  .brand__square {
    width: 60px;
    height: 60px;
    background: var(--mark-grey);
  }
  .brand__name {
    font-family: "Poppins", sans-serif;
    font-weight: 600;
    color: var(--silver);
    line-height: 1;
  }
  .brand__initials { display: block; font-size: 58px; letter-spacing: -1px; }
  .brand__rest { display: block; font-size: 11px; letter-spacing: 0.8px; text-transform: uppercase; margin-top: 2px; }
</style>
</head>
<body>
  <main class="card-set">
    <section class="card card--front" aria-label="Card front">
      <div class="identity">
        <p class="identity__name">TAMSIN CORVELL</p>
        <p class="identity__title">FOUNDER</p>
      </div>
      <span class="divider"></span>
      <ul class="contact-list">
        <li>
          <svg viewBox="0 0 10 10" aria-hidden="true"><path d="M1 3.5C1 2 2.5 1 5 1s4 1 4 2.5v1H7V3.6C6.4 3.3 3.6 3.3 3 3.6V4.5H1zM2.2 5h5.6L9 9H1z"/></svg>
          <span>000 000 0000</span>
        </li>
        <li>
          <svg viewBox="0 0 10 10" aria-hidden="true"><path d="M0 2h10v6H0zM0.8 2.6 5 5.6l4.2-3v0.9L5 6.5 0.8 3.5z" fill-rule="evenodd"/></svg>
          <span>info@yourmail.com</span>
        </li>
      </ul>
    </section>

    <section class="card card--back" aria-label="Card back">
      <div class="brand">
        <span class="brand__square" aria-hidden="true"></span>
        <p class="brand__name">
          <span class="brand__initials">KV</span>
          <span class="brand__rest">Field Inspections</span>
        </p>
      </div>
    </section>
  </main>
</body>
</html>
```